Complete Restaurant Branding Project

Bistro Velluto is looking for new ideas and designs for our various branded items.

You will be required to design the following items:

1) Staff Uniforms
2) Dine In Menu
3) Take Out Menu
4) Food Take Out Packaging
5) Take Out Bags
6) Beverage Take Out Cups
7) Dine in plates, coffee cups, mugs, etc...
8) Feel free to design any other brandable items related to our business

Please check our website to get a feel of our restaurant. Make sure to check the menu and the different dishes we offer to help you in the food packaging design and menu design. http://www.bistrovelluto-example.com/

We are open to new ideas, so we intentionally won't specify details such as materials, sizes, or shapes for any item.

We refined our logo in a contest a few days ago, the new logo is attached. Please don't use the logo from the website or any graphic elements from the website theme in your designs.

```html
<!DOCTYPE html>
<html lang="en">
<head>
<meta charset="utf-8">
<title>Bistro Velluto – Dish of the Day Table Tent</title>
<link href="https://fonts.googleapis.com/css2?family=Oswald:wght@700&family=Copse&display=swap" rel="stylesheet">
<style>
  :root {
    --kraft: #dcc49c;
    --kraft-light: #e6d2ad;
    --kraft-edge: #c9ad80;
    --band: #1f1d1a;
    --band-line: #3a3632;
    --ink: #1c1a17;
    --brand-red: #7a1f16;
    --leaf-dark: #3f7a2a;
    --leaf-light: #7fb24d;
    --photo-warm: #c8774a;
    --photo-cool: #5d7fa8;
    --paper-white: #fbfaf6;
  }
  * { margin: 0; padding: 0; box-sizing: border-box; }
  html, body { width: 1051px; height: 1200px; overflow: hidden; }
  body { background: #ffffff; }

  .table-tent {
    position: relative;
    width: 1051px;
    height: 1200px;
    background: radial-gradient(ellipse at 50% 45%, var(--kraft-light) 0%, var(--kraft) 60%, var(--kraft-edge) 100%);
    overflow: hidden;
  }

  .band {
    position: absolute;
    left: 0; right: 0;
    background: var(--band);
    border-color: var(--band-line);
    border-style: solid;
    border-width: 0;
  }
  .band--top { top: 0; height: 60px; border-bottom-width: 3px; }
  .band--bottom { bottom: 0; height: 90px; border-top-width: 3px; }

  .ivy-garland {
    position: absolute;
    top: 58px;
    left: 300px;
    width: 751px;
    height: 90px;
    background: linear-gradient(90deg, rgba(127,178,77,0) 0%, var(--leaf-light) 20%, var(--leaf-dark) 55%, var(--leaf-light) 85%, var(--leaf-dark) 100%);
    border-radius: 0 0 40px 60px;
    opacity: 0.85;
  }

  .brand {
    position: absolute;
    top: 165px;
    left: 0; right: 0;
    display: flex;
    flex-direction: column;
    align-items: center;
    gap: 10px;
  }
  .brand__dot {
    width: 96px; height: 96px;
    border-radius: 50%;
    background: var(--brand-red);
  }
  .brand__name {
    font-family: "Copse", serif;
    font-size: 24px;
    line-height: 1.2;
    color: var(--brand-red);
    letter-spacing: 1px;
  }

  .heading {
    position: absolute;
    top: 322px;
    left: 0; right: 0;
    text-align: center;
  }
  .heading__rule { display: block; margin: 0 auto; }
  .heading__title {
    font-family: "Oswald", sans-serif;
    font-weight: 700;
    font-size: 52px;
    color: var(--ink);
    letter-spacing: 1px;
    line-height: 1;
    margin: 10px 0;
  }

  .photo-stack {
    position: absolute;
    top: 450px;
    left: 205px;
    width: 640px;
    height: 360px;
  }
  .photo-stack__back,
  .photo-stack__front {
    position: absolute;
    inset: 0;
    background: var(--paper-white);
    box-shadow: 0 4px 10px rgba(0,0,0,0.25);
  }
  .photo-stack__back { transform: rotate(2deg) translate(14px, 6px); }
  .photo-stack__front { transform: rotate(-3deg); padding: 14px; }
  .photo-stack__image {
    width: 100%; height: 100%;
    background:
      radial-gradient(ellipse at 45% 65%, #e8a56a 0%, var(--photo-warm) 45%, rgba(200,119,74,0) 75%),
      linear-gradient(160deg, #b35a4a 0%, #d8c6b0 40%, var(--photo-cool) 75%, #e9e6df 100%);
  }

  .dish {
    position: absolute;
    top: 865px;
    left: 60px; right: 60px;
    text-align: center;
    color: var(--ink);
    font-family: "Copse", serif;
  }
  .dish__name { font-size: 50px; font-weight: 400; line-height: 1.1; }
  .dish__description { font-size: 28px; line-height: 1.3; margin-top: 8px; }
</style>
</head>
<body>
  <main class="table-tent">
    <div class="band band--top"></div>
    <div class="ivy-garland" role="img" aria-label="Trailing ivy vine with green leaves along the top edge"></div>

    <header class="brand">
      <div class="brand__dot"></div>
      <div class="brand__name">Bistro Velluto</div>
    </header>

    <section class="heading">
      <svg class="heading__rule" width="460" height="14" viewBox="0 0 460 14">
        <line x1="10" y1="7" x2="450" y2="7" stroke="#1c1a17" stroke-width="2"/>
        <rect x="224" y="1" width="12" height="12" transform="rotate(45 230 7)" fill="#1c1a17"/>
        <rect x="0" y="3" width="8" height="8" transform="rotate(45 4 7)" fill="#1c1a17"/>
        <rect x="452" y="3" width="8" height="8" transform="rotate(45 456 7)" fill="#1c1a17"/>
      </svg>
      <h1 class="heading__title">DISH OF THE DAY</h1>
      <svg class="heading__rule" width="460" height="14" viewBox="0 0 460 14">
        <line x1="10" y1="7" x2="450" y2="7" stroke="#1c1a17" stroke-width="2"/>
        <rect x="224" y="1" width="12" height="12" transform="rotate(45 230 7)" fill="#1c1a17"/>
        <rect x="0" y="3" width="8" height="8" transform="rotate(45 4 7)" fill="#1c1a17"/>
        <rect x="452" y="3" width="8" height="8" transform="rotate(45 456 7)" fill="#1c1a17"/>
      </svg>
    </section>

    <figure class="photo-stack">
      <div class="photo-stack__back"></div>
      <div class="photo-stack__front">
        <div class="photo-stack__image" role="img" aria-label="Plate of pasta with shrimp, tomato, parsley and a lemon wedge"></div>
      </div>
    </figure>

    <section class="dish">
      <h2 class="dish__name">Penne Gratin</h2>
      <p class="dish__description">Penne with chicken, mushrooms, and cauliflower<br>cooked in a creamy cheese sauce topped with<br>mozzarella and parmesan cheese.</p>
    </section>

    <div class="band band--bottom"></div>
  </main>
</body>
</html>
```